Velmora Water Purification

We need a website set up on a "Free account" WordPress platform. (This is the type of Wordpress site that you can sign up for and create online for free (not a server-hosted type.)
The website will be for a water purification company. They install devices in homes to purify the water for safer drinking, bathing, and cleaning.
Our logo is attached. Please keep color scheme of the website consistent with the logo.
Water Purification

```html
<!DOCTYPE html>
<html lang="en">
<head>
<meta charset="utf-8">
<title>Velmora Water Purification</title>
<link rel="stylesheet" href="https://fonts.googleapis.com/css2?family=Open+Sans:ital,wght@0,400;0,600;0,700;1,400&display=swap">
<style>
:root{
  --admin-bar:#0a0a0a;
  --nav-blue:#2ea3f2;
  --ink:#333333;
  --ink-soft:#666666;
  --band-dark:#363b43;
  --teal:#7bb9c1;
  --teal-icon:#6fb3bd;
  --line:#d9d9d9;
  --panel:#f4f4f4;
  --cta-red:#f64a46;
  --white:#ffffff;
}
*{box-sizing:border-box;margin:0;padding:0}
html,body{width:1200px;height:2687px;overflow:hidden}
body{font-family:"Open Sans",Arial,sans-serif;color:var(--ink);background:var(--white);font-size:14px;line-height:24px}
.container{position:relative;width:972px;margin:0 auto}

.admin-bar{height:33px;background:var(--admin-bar)}
.site-nav{height:41px;background:var(--nav-blue);display:flex;justify-content:flex-end;align-items:center;padding-right:18px;gap:24px}
.site-nav a{color:var(--white);text-decoration:none;font-weight:600;font-size:16px}

.hero{position:relative;height:475px;background:linear-gradient(170deg,#9fb4c0 0%,#d8e1e6 35%,#6f8c9c 60%,#2f5064 100%)}
.hero-brand{position:absolute;left:180px;top:180px;width:400px;display:flex;align-items:center;gap:18px}
.hero-brand .dot{width:46px;height:46px;border-radius:50%;background:#1f5fae;flex:none}
.hero-brand span{font-size:36px;font-weight:700;line-height:44px;color:#1f5fae}
.hero-text{position:absolute;left:630px;top:130px;width:480px}
.hero-text h1{font-size:45px;line-height:46px;font-weight:700;color:#2b2b2b}
.hero-text p{font-size:19px;font-weight:700;margin-top:10px;color:#222}
.btn-outline{display:inline-block;margin-top:26px;padding:6px 20px;font-size:20px;color:var(--white);border:2px solid var(--white);background:rgba(46,163,242,.55);text-decoration:none}

.features{height:224px;background:var(--band-dark)}
.features .container{display:flex;justify-content:space-between;padding-top:25px;width:1020px}
.feature{width:250px;text-align:center;color:var(--white);font-size:17px}
.feature svg{display:block;margin:0 auto 26px;height:96px}

.offer{height:280px;border-bottom:1px solid #eee}
.offer h2,.benefits h2,.faq h2{font-weight:400;font-size:27px;line-height:34px}
.offer h2{padding-top:32px}
.tabs{position:absolute;left:0;top:92px;width:629px;border:1px solid var(--line)}
.tab-row{display:flex;background:var(--panel);border-bottom:1px solid var(--line)}
.tab-row span{font-size:13px;padding:4px 22px;border-right:1px solid var(--line);color:#555}
.tab-row .active{background:var(--white);font-weight:600;color:#222}
.tab-body{padding:20px 30px 24px;font-size:13.5px;line-height:23px;color:var(--ink-soft);height:140px}
.skills{position:absolute;left:684px;top:92px;width:288px}
.skill{margin-bottom:14px}
.skill small{display:block;font-size:12px;line-height:17px;color:var(--ink-soft)}
.skill .track{height:20px;background:#f0f0f0}
.skill .fill{height:20px;background:var(--teal);color:var(--white);font-size:12px;font-weight:700;text-align:right;padding-right:8px;line-height:20px}

.benefits{height:364px}
.jar-photo{position:absolute;left:0;top:6px;width:458px;height:307px;background:radial-gradient(circle at 45% 45%,#9aa09a 0%,#4b504c 40%,#111 85%)}
.benefit-list{position:absolute;left:512px;top:0;width:460px}
.benefits h2{padding-top:10px;margin-bottom:20px}
.benefit{position:relative;padding-left:46px;margin-bottom:24px}
.benefit .ico{position:absolute;left:0;top:3px;width:28px;height:28px;border-radius:50%;background:var(--teal-icon)}
.benefit h3{font-size:18px;font-weight:400;line-height:24px;color:#333}
.benefit p{font-size:13.5px;line-height:23px;color:var(--ink-soft)}

.water-banner{height:473px;background:linear-gradient(160deg,#1fa7c4 0%,#4fd0d9 40%,#23a8c2 70%,#1591b4 100%);display:flex;align-items:center;justify-content:center;gap:22px}
.water-banner .dot{width:60px;height:60px;border-radius:50%;background:#0d3f8a}
.water-banner span{font-size:56px;font-weight:700;color:#0d3f8a}

.faq{height:373px}
.faq-text{position:absolute;left:-2px;top:24px;width:460px}
.faq-text p{font-size:13.5px;line-height:23px;color:var(--ink-soft);margin-top:4px}
.accordion{position:absolute;left:512px;top:30px;width:460px}
.acc-item{border:1px solid var(--line);margin-bottom:28px;padding:16px 20px;font-size:15px;background:var(--panel);display:flex;justify-content:space-between;align-items:center}
.acc-item.open{background:var(--white);display:block}
.acc-item.open p{font-size:13.5px;line-height:23px;color:var(--ink-soft);margin-top:14px}
.acc-item .plus{width:14px;height:14px;border-radius:50%;background:#c8c8c8}

.reviews{height:239px}
.reviews .container{display:flex;justify-content:space-between;width:1000px;padding-top:24px}
.review{position:relative;width:288px;height:172px;background:var(--panel);margin-top:18px;text-align:center;padding:36px 28px 0}
.review svg{position:absolute;left:128px;top:-18px}
.review q{display:block;font-style:italic;font-size:13px;line-height:21px;color:var(--ink-soft);quotes:"\201C" "\201D"}
.review cite{display:block;font-style:normal;font-weight:700;font-size:13px;margin-top:16px;color:#444}

.cta{height:185px;background:var(--cta-red);color:var(--white);text-align:center;padding-top:22px}
.cta h2{font-size:28px;font-weight:400;line-height:36px}
.cta p{font-size:14px;margin-top:6px}
.cta a{display:inline-block;margin-top:20px;border:2px solid var(--white);color:var(--white);text-decoration:none;font-size:20px;padding:8px 20px}
</style>
</head>
<body>
<div class="admin-bar"></div>
<nav class="site-nav"><a href="#">Home</a><a href="#">About Us</a><a href="#">Contact Us</a></nav>

<header class="hero" role="img" aria-label="Photograph of splashing clear water">
  <div class="hero-brand"><div class="dot"></div><span>Velmora Water Purification</span></div>
  <div class="hero-text">
    <h1>Velmora Water Purification</h1>
    <p>Changing the way of water purification.</p>
    <a class="btn-outline" href="#">Learn More</a>
  </div>
</header>

<section class="features">
  <div class="container">
    <div class="feature">
      <svg viewBox="0 0 100 100" width="100" fill="none" stroke="#6fb3bd" stroke-width="4" stroke-linejoin="round"><path d="M8 50 L50 10 L92 50"/><path d="M20 40 V92 H80 V40"/><path d="M42 92 V64 H58 V92"/><path d="M70 22 V36"/></svg>
      See the Difference
    </div>
    <div class="feature">
      <svg viewBox="0 0 110 100" width="110" fill="none" stroke="#6fb3bd" stroke-width="4"><path d="M12 28 H82 V58 Q82 84 47 84 Q12 84 12 58 Z"/><path d="M82 38 Q102 38 98 52 Q94 64 80 64"/></svg>
      Taste the Difference
    </div>
    <div class="feature">
      <svg viewBox="0 0 100 100" width="100" fill="none" stroke="#6fb3bd" stroke-width="4"><path d="M50 90 L14 52 Q2 36 14 22 Q30 6 50 28 Q70 6 86 22 Q98 36 86 52 Z"/></svg>
      Feel the Difference
    </div>
    <div class="feature">
      <svg viewBox="0 0 100 100" width="100" fill="none" stroke="#6fb3bd" stroke-width="4" stroke-linejoin="round"><path d="M10 44 H26 V88 H10 Z"/><path d="M26 48 L44 24 Q48 6 58 12 Q62 22 56 40 H84 Q94 42 90 54 Q94 62 86 66 Q90 76 80 78 Q82 88 70 88 H26"/></svg>
      Save Money
    </div>
  </div>
</section>

<section class="offer">
  <div class="container">
    <h2>What We Offer</h2>
    <div class="tabs">
      <div class="tab-row"><span class="active">Overview</span><span>Mission Statement</span><span>Culture</span></div>
      <div class="tab-body">Aenean consectetur ipsum ante, vel egestas enim tincidunt quis. Pellentesque vitae congue neque, vel mattis ante. In vitae tempus nunc. Etiam adipiscing enim sed condimentum ultrices. Aenean consectetur ipsum ante, vel egestas enim tincidunt quis. Pellentesque vitae congue neque, vel mattis ante.</div>
    </div>
    <div class="skills">
      <div class="skill"><small>Better Taste.</small><div class="track"><div class="fill" style="width:90%">90%</div></div></div>
      <div class="skill"><small>Better Smell.</small><div class="track"><div class="fill" style="width:85%">85%</div></div></div>
      <div class="skill"><small>Better Feel.</small><div class="track"><div class="fill" style="width:95%">95%</div></div></div>
    </div>
  </div>
</section>

<section class="benefits">
  <div class="container">
    <div class="jar-photo" role="img" aria-label="Photograph of a glass jar of water on a table in window light"></div>
    <div class="benefit-list">
      <h2>Our Benefits</h2>
      <div class="benefit"><div class="ico"></div><h3>It does not add harmful chemicals to the water.</h3><p>Aenean consectetur ipsum ante, vel egestas enim tincidunt quis. Pellentesque vitae congue neque, vel mattis ante.</p></div>
      <div class="benefit"><div class="ico"></div><h3>It does not change the smell, taste or color.</h3><p>Aenean consectetur ipsum ante, vel egestas enim tincidunt quis. Pellentesque vitae congue neque, vel mattis ante.</p></div>
      <div class="benefit"><div class="ico"></div><h3>It is compact and easy to maintain.</h3><p>Aenean consectetur ipsum ante, vel egestas enim tincidunt quis. Pellentesque vitae congue neque, vel mattis ante.</p></div>
    </div>
  </div>
</section>

<section class="water-banner" role="img" aria-label="Photograph of rippling turquoise pool water with the company name">
  <div class="dot"></div><span>Velmora Water Purification</span>
</section>

<section class="faq">
  <div class="container">
    <div class="faq-text">
      <h2>Frequently Asked Questions</h2>
      <p>Lorem ipsum dolor sit amet, consectetur adipiscing elit. Nunc aliquam justo et nibh venenatis aliquet. Morbi mollis mollis pellentesque. Aenean vitae erat velit. Maecenas urna sapien, dignissim a augue vitae, porttitor luctus urna. Morbi scelerisque semper congue. Donec vitae congue quam. Pellentesque convallis est a eros porta, ut porttitor magna convallis. Donec quis felis imperdiet, vestibulum est ut, pulvinar dolor. Mauris laoreet varius sem, tempus congue nibh elementum facilisis. Aliquam ut odio risus. Mauris consectetur mi et ante aliquam, eget posuere urna semper. Vestibulum vestibulum rhoncus enim, id iaculis eros commodo non.</p>
    </div>
    <div class="accordion">
      <div class="acc-item open">What kind of clients do you work with?<p>Lorem ipsum dolor sit amet, consectetur adipiscing elit. Nunc aliquam justo et nibh venenatis aliquet.</p></div>
      <div class="acc-item">What is your turn around time?<span class="plus"></span></div>
      <div class="acc-item">Do you have an affiliate program?<span class="plus"></span></div>
    </div>
  </div>
</section>

<section class="reviews">
  <div class="container">
    <div class="review">
      <svg width="34" height="34" viewBox="0 0 34 34" fill="none" stroke="#444" stroke-width="2.5"><circle cx="17" cy="17" r="15"/><path d="M11 20 Q10 13 15 11 M18 20 Q17 13 22 11"/><circle cx="12" cy="20" r="2" fill="#444"/><circle cx="19" cy="20" r="2" fill="#444"/></svg>
      <q>We are very pleased with the sales person, the technician, and are very pleased with the equipment.</q>
      <cite>Customer Review 1</cite>
    </div>
    <div class="review">
      <svg width="34" height="34" viewBox="0 0 34 34" fill="none" stroke="#444" stroke-width="2.5"><circle cx="17" cy="17" r="15"/><path d="M11 20 Q10 13 15 11 M18 20 Q17 13 22 11"/><circle cx="12" cy="20" r="2" fill="#444"/><circle cx="19" cy="20" r="2" fill="#444"/></svg>
      <q>I love the water system and have already recommended to my boss!</q>
      <cite>Customer Review 2</cite>
    </div>
    <div class="review">
      <svg width="34" height="34" viewBox="0 0 34 34" fill="none" stroke="#444" stroke-width="2.5"><circle cx="17" cy="17" r="15"/><path d="M11 20 Q10 13 15 11 M18 20 Q17 13 22 11"/><circle cx="12" cy="20" r="2" fill="#444"/><circle cx="19" cy="20" r="2" fill="#444"/></svg>
      <q>My sales person was very professional and very knowledgeable!</q>
      <cite>Customer Review 3</cite>
    </div>
  </div>
</section>

<section class="cta">
  <h2>Questions?</h2>
  <p>Drop us a line anytime, and one of our customer service reps will respond to you as soon as possible</p>
  <a href="#">Email</a>
</section>
</body>
</html>
```